依頼詳細
科学に興味のある中学生・高校生に訴求したいです。(女子の受講生が多くなると嬉しいです)イラストを入れていただき、見やすく、親しみやすくしていただきたいです。(ロゴは目立たなくてもいいです)コメントをしている受講生の写真は切り抜き希望です。
記載項目
原案添付します
サイズ
A4
ページ数
両面
希望イメージ
シンプル 複雑
単色 カラフル
暗い 明るい
日常 高級
遊び心 厳粛
未来的 伝統的
女性的 男性的
希望する色
赤系
納品ファイル
• イラストレーター形式 (.ai)
補足説明
■ 選んだ理由

甘くなりすぎず、硬すぎずのちょうどよいバランスがよかったです。

■ 提案者全員のお礼・コメント

皆様お忙しい中お時間を割いてたくさんご提案くださり、誠にありがとうございます。大変感謝しております。どのご提案も素晴しく、非常に悩みました。またの機会がございましたら、是非よろしくお願いいたします。
本当にありがとうございました。

```html
<!DOCTYPE html>
<html lang="ja">
<head>
<meta charset="utf-8">
<title>SPARK 受講コース案内</title>
<link rel="stylesheet" href="https://fonts.googleapis.com/css2?family=M+PLUS+Rounded+1c:wght@400;700;800&display=swap">
<style>
:root{
  --bg:#fdeef0;
  --orange:#f0871e;
  --orange-soft:#fde3c6;
  --pink:#e65772;
  --pink-soft:#fbd6dd;
  --red:#d9443e;
  --ink:#4e3428;
  --white:#ffffff;
  --footer:#ffffff;
}
*{box-sizing:border-box;margin:0;padding:0}
html,body{width:846px;height:1200px;overflow:hidden}
body{background:var(--bg);font-family:"M PLUS Rounded 1c",sans-serif;color:var(--ink);position:relative}
.abs{position:absolute}
.course-band{position:absolute;left:0;width:846px;height:64px;border-radius:0 32px 32px 0}
.course-title{position:absolute;left:22px;font-weight:800;font-size:30px;color:var(--white);letter-spacing:2px;white-space:nowrap}
.course-title.compact{font-size:27px;letter-spacing:1px}
.course-title small{font-size:18px}
.info-box{position:absolute;right:18px;width:380px;background:var(--white);border-radius:10px;padding:10px 14px;font-size:11px;line-height:1.6;border:2px solid}
.info-box.narrow{width:270px}
.info-box dt{float:left;width:64px;font-weight:700;color:var(--white);border-radius:3px;text-align:center;margin-right:8px;margin-bottom:3px}
.info-box dd{margin-bottom:3px}
.body-text{position:absolute;font-size:12.5px;line-height:1.75}
.sub-head{font-weight:800;font-size:14px;margin-bottom:4px}
.list{list-style:none;font-size:11.5px;line-height:1.7}
.voice{position:absolute;background:var(--white);border-radius:14px;padding:14px 16px;font-size:12px;line-height:1.75;border:2px solid}
.photo{position:absolute;border-radius:50% 50% 12px 12px;background:linear-gradient(#f3c9a8,#d9a07e)}
.illust{position:absolute;border-radius:16px}
.achieve{position:absolute;background:var(--white);border:2px dashed var(--orange);border-radius:12px;padding:12px 14px}
.footer{position:absolute;left:0;top:1112px;width:846px;height:88px;background:var(--footer);border-top:4px solid var(--pink)}
.brand{position:absolute;left:30px;top:22px;display:flex;align-items:center;gap:8px;font-weight:800;font-size:22px;color:var(--pink)}
.brand .dot{width:22px;height:22px;border-radius:50%;background:var(--pink)}
.office{position:absolute;left:190px;top:14px;font-weight:800;font-size:24px;color:var(--ink)}
.contact{position:absolute;left:190px;top:50px;font-weight:700;font-size:17px;color:var(--ink);word-spacing:40px}
</style>
</head>
<body>

<!-- チャレンジコース -->
<div class="course-band" style="top:14px;background:var(--orange)"></div>
<h2 class="course-title" style="top:26px">チャレンジコース</h2>
<dl class="info-box" style="top:20px;border-color:var(--orange)">
  <dt style="background:var(--orange)">募集対象</dt><dd>科学に興味のある中学生・高校生</dd>
  <dt style="background:var(--orange)">応募期間</dt><dd>5月上旬〜6月中旬(予定)</dd>
  <dt style="background:var(--orange)">受講期間</dt><dd>7月〜翌年3月</dd>
  <dt style="background:var(--orange)">受講料</dt><dd>無料</dd>
</dl>
<p class="body-text" style="left:22px;top:145px;width:400px">2ヶ月に1度行われる共通プログラムに参加することで、幅広く科学に触れます。SSコースやTLコース生と意見交換も行うので、自分がやりたいことを見つけていってください。研究テーマ・学習が好きな人、将来を見つけたい人は、SSコース・TLコースへの参加も可能です。</p>
<div class="photo" role="img" aria-label="チャレンジコース受講生の切り抜き写真" style="left:285px;top:280px;width:120px;height:125px"></div>
<div class="voice" style="left:22px;top:280px;width:250px;border-color:var(--orange)">SPARKを受講して、サイエンスの面白さを知りました。分からないことも大学の先生に気軽に質問できて、もっと研究してみたいという気持ちが強くなりました。</div>
<div class="achieve" style="left:440px;top:150px;width:388px;height:250px">
  <p class="sub-head" style="color:var(--orange)">SPARK生の実績</p>
  <p class="sub-head" style="font-size:12px">&lt;SSコース&gt;</p>
  <ul class="list">
    <li>・全国高校生科学研究発表会 奨励賞</li>
    <li>・日本学生科学コンテスト 県代表</li>
    <li>・国際科学フェア 出場</li>
    <li>・学会ジュニアセッション 優秀発表賞</li>
  </ul>
  <p class="sub-head" style="font-size:12px;margin-top:6px">&lt;TLコース&gt;</p>
  <ul class="list">
    <li>・科学オリンピック 本選出場</li>
    <li>・数学コンテスト 銀賞</li>
    <li>・海外研修プログラム 派遣</li>
  </ul>
</div>

<!-- スーパーサイエンスコース -->
<div class="course-band" style="top:445px;background:var(--pink)"></div>
<h2 class="course-title compact" style="top:459px">スーパーサイエンスコース<small>(SSコース)</small></h2>
<dl class="info-box narrow" style="top:450px;border-color:var(--pink)">
  <dt style="background:var(--pink)">募集対象</dt><dd>研究テーマを持つ中高生</dd>
  <dt style="background:var(--pink)">受講期間</dt><dd>1年間(継続可)</dd>
</dl>
<p class="body-text" style="left:22px;top:528px;width:380px">一人ひとりの研究テーマにあわせて、大学教員と大学院生が専属のアドバイザーとして研究をサポートします。研究成果は学会やコンテストで発表します。</p>
<div class="illust" role="img" aria-label="中高生3名と大学教員・大学院生5名が1年間研究を進める図解イラスト" style="left:410px;top:528px;width:420px;height:110px;background:linear-gradient(90deg,var(--orange-soft),var(--pink-soft))"></div>
<div class="abs" style="left:22px;top:650px;width:330px">
  <p class="sub-head" style="color:var(--pink)">SS研究の研究テーマ例</p>
  <ul class="list">
    <li>・身近な植物に含まれる色素の分析</li>
    <li>・微生物を使った水質浄化の研究</li>
    <li>・振り子の周期と空気抵抗の関係</li>
    <li>・昆虫の行動パターンの観察と解析</li>
  </ul>
</div>
<div class="photo" role="img" aria-label="SSコース受講生の切り抜き写真" style="left:360px;top:645px;width:110px;height:135px"></div>
<div class="voice" style="left:485px;top:650px;width:340px;border-color:var(--pink)">研究の進め方を一から教えていただき、自分の力で実験を計画できるようになりました。学会での発表は緊張しましたが、大きな自信につながりました。</div>

<!-- 科学トップリーダーコース -->
<div class="course-band" style="top:805px;background:var(--red)"></div>
<h2 class="course-title compact" style="top:819px">科学トップリーダーコース<small>(TLコース)</small></h2>
<dl class="info-box narrow" style="top:810px;border-color:var(--red)">
  <dt style="background:var(--red)">募集対象</dt><dd>科学オリンピック等を目指す生徒</dd>
  <dt style="background:var(--red)">受講期間</dt><dd>5月〜翌年3月</dd>
</dl>
<p class="body-text" style="left:22px;top:884px;width:400px">物理・化学・生物・数学・情報などの分野で、大学教員による発展的な講義と演習を受けます。科学オリンピックや海外研修への挑戦を通して、世界で活躍する力を伸ばします。</p>
<div class="illust" role="img" aria-label="物理・化学・生物・数学をイメージした科学のイラスト" style="left:440px;top:880px;width:390px;height:80px;background:linear-gradient(90deg,var(--pink-soft),var(--orange-soft))"></div>
<div class="abs" style="left:22px;top:975px;width:330px">
  <p class="sub-head" style="color:var(--red)">分野別研究室の例</p>
  <ul class="list">
    <li>【物理】光と波の性質を実験で探る</li>
    <li>【化学】有機合成と分析の基礎</li>
    <li>【生物】遺伝子と細胞のしくみ</li>
    <li>【数学】整数論と組合せの問題演習</li>
  </ul>
</div>
<div class="photo" role="img" aria-label="TLコース受講生の切り抜き写真" style="left:360px;top:972px;width:110px;height:132px"></div>
<div class="voice" style="left:485px;top:975px;width:340px;border-color:var(--red)">大学の先生の講義はとても刺激的で、学校では学べない内容にわくわくしました。同じ目標を持つ仲間と出会えたことも大きな財産です。</div>

<!-- フッター -->
<footer class="footer">
  <div class="brand"><span class="dot"></span>SPARK</div>
  <p class="office">みらい科学大学 社会連携課 SPARK事務局</p>
  <p class="contact">info@spark.mirai-u.ac.jp http://spark.mirai-u.ac.jp/</p>
</footer>

</body>
</html>
```